Defense contractor needs a roll-up for an exhibition

The booth we have booked has only a size of 3m².
So this will be the centerpiece of the whole booth.
We need a roll-up that attracts visitors and at the same time it should contain already designed graphics. These graphics are giving visitors an overview of our system. So it is necessary to have them exposed in a height that the booth personal can conveniently point with its fingers at them.
For information about our company and product visit:
https://www.corvantilmetrics.com/
For designing you should use Adobe Illustrator and the templates provided in the zip file, to guarantee a perfect print.
I have supplied my business card that you can copy the logo. As the company logo will be already at the booth nearby the top of the roll-up, you should not place it there. It can be in the middle or at the bottom.
I have uploaded a picture of the booth. The roll up will be placed at the left of the screen and has a size of 80cm x 200cm

Defense

Defense

Serif

0054AA
0677BA
7BADD7
CADEEF
E8F1F8

Must have
• you must use the Adobe Illustrator template to have a good printing result
Should not have
• company logo on the upper side of the roll-up

```html
<!DOCTYPE html>
<html lang="en">
<head>
<meta charset="utf-8">
<title>Advanced Combat Training Systems – Roll-up</title>
<link rel="stylesheet" href="https://fonts.googleapis.com/css2?family=Oswald:wght@400;500;700&family=Montserrat:wght@500;700;800&display=swap">
<style>
  :root{
    --page:#d9d9db;
    --navy:#15205a;
    --royal:#2747b8;
    --cyan:#12b6f5;
    --band-blue:#1578f5;
    --ink:#000000;
    --deep:#06283b;
    --white:#ffffff;
    --panel:#e6eaf5;
  }
  *{box-sizing:border-box;margin:0;padding:0}
  html,body{width:1200px;height:2486px;overflow:hidden;background:var(--page)}
  .rollup{
    position:absolute;left:110px;top:45px;width:980px;height:2396px;
    overflow:hidden;background:var(--ink);
    box-shadow:0 6px 18px rgba(0,0,0,.25);
  }
  .hero-scene{
    position:absolute;left:0;top:0;width:980px;height:1390px;
    background:
      radial-gradient(ellipse 60% 22% at 50% 60%, rgba(255,190,205,.85), rgba(255,190,205,0) 70%),
      radial-gradient(ellipse 45% 18% at 30% 72%, rgba(210,230,255,.9), rgba(210,230,255,0) 70%),
      linear-gradient(180deg,var(--navy) 0%,var(--royal) 30%,#6e7fd6 48%,#d9a6c8 62%,#8fb6ea 74%,#101322 84%,#000 100%);
  }
  .headline{position:absolute;left:0;top:130px;width:980px;height:460px}
  .headline text{font-family:'Oswald',sans-serif}
  .features{
    position:absolute;left:0;top:1221px;width:980px;height:166px;
    background:linear-gradient(180deg,rgba(0,0,0,.55),#000 60%);
    font-family:'Montserrat',sans-serif;color:var(--white);
  }
  .features-label{position:absolute;left:70px;top:60px;font-weight:800;font-size:32px;letter-spacing:.5px}
  .features-label::after{content:"";display:inline-block;margin-left:10px;border-left:14px solid var(--band-blue);border-top:9px solid transparent;border-bottom:9px solid transparent}
  .feature{position:absolute;top:26px;font-weight:500;font-size:28px;line-height:34px}
  .feature.f1{left:312px}.feature.f2{left:525px}.feature.f3{left:770px}
  .divider{position:absolute;top:30px;width:2px;height:100px;background:rgba(255,255,255,.7)}
  .divider.d1{left:488px}.divider.d2{left:730px}
  .system-band{position:absolute;left:0;top:1386px;width:980px;height:214px;background:var(--band-blue)}
  .applications{
    position:absolute;left:0;top:1600px;width:980px;height:796px;
    background:linear-gradient(180deg,#000 0%,#03141f 45%,var(--deep) 100%);
    color:var(--white);text-align:center;
  }
  .section-title{position:absolute;top:52px;width:100%;font-family:'Montserrat',sans-serif;font-weight:800;font-size:46px;letter-spacing:1px}
  .app{position:absolute;top:146px;width:220px;text-align:center}
  .app svg{display:block;margin:0 auto}
  .app-name{margin-top:16px;font-family:'Oswald',sans-serif;font-weight:500;font-size:32px;line-height:40px;text-transform:uppercase;letter-spacing:-.5px}
  .app.a1{left:57px}.app.a2{left:277px}.app.a3{left:493px}.app.a4{left:708px}
  .pager{position:absolute;top:432px;left:0;width:100%;display:flex;justify-content:center;gap:8px}
  .pager span{width:11px;height:11px;border-radius:50%;background:var(--band-blue)}
  .pager span.on{background:var(--cyan)}
  .blurb{position:absolute;top:474px;width:100%;font-family:'Montserrat',sans-serif;font-weight:500;font-size:27px;line-height:34px}
  .sponsor{position:absolute;top:615px;width:100%;display:flex;justify-content:center;align-items:center;gap:18px;font-family:'Montserrat',sans-serif;font-weight:800;font-size:54px;letter-spacing:1px;text-transform:uppercase}
  .sponsor-dot{width:26px;height:26px;border-radius:50%;background:var(--white)}
</style>
</head>
<body>
<main class="rollup">
  <div class="hero-scene" role="img" aria-label="Battle tank silhouette with machine gun turret in tall grass against a pink and blue dusk sky, faint helicopters in the distance"></div>

  <svg class="headline" viewBox="0 0 980 460" width="980" height="460">
    <text x="112" y="158" fill="var(--cyan)" font-weight="700" font-size="190" textLength="762" lengthAdjust="spacingAndGlyphs">ADVANCED</text>
    <text x="112" y="352" fill="var(--white)" font-weight="700" font-size="238" textLength="756" lengthAdjust="spacingAndGlyphs">COMBAT</text>
    <text x="114" y="438" fill="var(--white)" font-weight="500" font-size="80" textLength="752" lengthAdjust="spacing">TRAINING SYSTEMS</text>
  </svg>

  <section class="features">
    <div class="features-label">FEATURES</div>
    <p class="feature f1">Full<br>instructor<br>overview</p>
    <span class="divider d1"></span>
    <p class="feature f2">All weather,<br>all terrain</p>
    <span class="divider d2"></span>
    <p class="feature f3">Full data<br>recording</p>
  </section>

  <svg class="system-band" viewBox="0 0 980 214" width="980" height="214">
    <polygon points="0,214 0,120 60,0 110,0 0,214" fill="#0b3f9a" opacity=".5"/>
    <polygon points="170,14 540,14 440,200 70,200" fill="var(--panel)" stroke="var(--ink)" stroke-width="10" role="img" aria-label="Isometric illustration of a mobile command truck with instructor stations and tanks on a training field"/>
    <polygon points="170,14 540,14 440,200 70,200" fill="none" stroke="var(--white)" stroke-width="3"/>
    <polygon points="560,14 935,14 835,200 460,200" fill="var(--panel)" stroke="var(--ink)" stroke-width="10" role="img" aria-label="Isometric illustration of a debriefing room with display screens and rows of seated trainees"/>
    <polygon points="560,14 935,14 835,200 460,200" fill="none" stroke="var(--white)" stroke-width="3"/>
    <polygon points="980,0 960,0 860,214 980,214" fill="#0b3f9a" opacity=".5"/>
  </svg>

  <section class="applications">
    <h2 class="section-title">APPLICATIONS</h2>

    <div class="app a1">
      <svg width="146" height="146" viewBox="0 0 146 146" aria-hidden="true">
        <circle cx="73" cy="73" r="70" fill="#1d2a36"/><circle cx="73" cy="70" r="66" fill="var(--white)"/><circle cx="73" cy="70" r="58" fill="var(--cyan)"/>
        <g fill="var(--white)"><rect x="52" y="50" width="36" height="16" rx="4"/><rect x="86" y="54" width="30" height="5"/><rect x="34" y="66" width="78" height="14" rx="4"/>
        <circle cx="46" cy="88" r="6"/><circle cx="62" cy="88" r="6"/><circle cx="78" cy="88" r="6"/><circle cx="94" cy="88" r="6"/></g>
      </svg>
      <p class="app-name">Duel<br>Simulation</p>
    </div>

    <div class="app a2">
      <svg width="146" height="146" viewBox="0 0 146 146" aria-hidden="true">
        <circle cx="73" cy="73" r="70" fill="#1d2a36"/><circle cx="73" cy="70" r="66" fill="var(--white)"/><circle cx="73" cy="70" r="58" fill="var(--cyan)"/>
        <g fill="none" stroke="var(--white)" stroke-width="5"><circle cx="73" cy="70" r="30"/><circle cx="73" cy="70" r="14"/>
        <line x1="73" y1="30" x2="73" y2="110"/><line x1="33" y1="70" x2="113" y2="70"/></g>
      </svg>
      <p class="app-name">Firing Range<br>Training</p>
    </div>

    <div class="app a3">
      <svg width="146" height="146" viewBox="0 0 146 146" aria-hidden="true">
        <circle cx="73" cy="73" r="70" fill="#1d2a36"/><circle cx="73" cy="70" r="66" fill="var(--white)"/><circle cx="73" cy="70" r="58" fill="var(--cyan)"/>
        <circle cx="73" cy="70" r="32" fill="none" stroke="var(--white)" stroke-width="9"/>
        <path d="M43 64 Q73 52 103 64 L86 76 L60 76 Z" fill="var(--white)"/><rect x="67" y="72" width="12" height="28" fill="var(--white)"/>
        <circle cx="73" cy="72" r="6" fill="var(--cyan)"/>
      </svg>
      <p class="app-name">Driving<br>Training</p>
    </div>

    <div class="app a4">
      <svg width="146" height="146" viewBox="0 0 146 146" aria-hidden="true">
        <circle cx="73" cy="73" r="70" fill="#1d2a36"/><circle cx="73" cy="70" r="66" fill="var(--white)"/><circle cx="73" cy="70" r="58" fill="var(--cyan)"/>
        <rect x="42" y="40" width="62" height="36" fill="none" stroke="var(--white)" stroke-width="4"/>
        <g fill="var(--white)"><circle cx="56" cy="62" r="5"/><rect x="50" y="68" width="12" height="10"/><line x1="62" y1="64" x2="80" y2="52" stroke="var(--white)" stroke-width="3"/>
        <circle cx="48" cy="88" r="5"/><circle cx="64" cy="88" r="5"/><circle cx="82" cy="88" r="5"/><circle cx="98" cy="88" r="5"/>
        <rect x="42" y="94" width="12" height="8"/><rect x="58" y="94" width="12" height="8"/><rect x="76" y="94" width="12" height="8"/><rect x="92" y="94" width="12" height="8"/></g>
      </svg>
      <p class="app-name">Debriefing</p>
    </div>

    <div class="pager"><span></span><span></span><span class="on"></span><span class="on"></span><span></span><span></span></div>

    <p class="blurb">Fully deployed in 20 minutes or less, VARTEK is uniquely<br>designed to outfit armored vehicles and weapons systems</p>

    <div class="sponsor"><span class="sponsor-dot"></span><span>Corvantil Metrics</span></div>
  </section>
</main>
</body>
</html>
```